Harwick Legal

To update and modernize current business card appearance. Marta's business is based in Melbourne with 4 other lawyers in the firm. Marta travels to the Pilbara in Western Australia approximately 1 week a month as part of the firms legal work. She consults with clients in Newman, Tom Price and Port Hedland. The lawyers work mostly from a home office, apart from court appearances. They have a virtual office in Melbourne city, and use facilities in 3 or 4 other locations around Melbourne. It is important the client's think this is a conventional law firm with a permanent office. Our business structure is a difficult concept for them to grasp. The business has been operational for 3 years, growing from 1 lawyer to 4 lawyers during that time. Our website is www.Harwicklegal.example.au and is currently being upgraded as we are not happy with its content. The logo is currently orange and dark grey but the orange is a difficult colour to reproduce and often turns out "poo" brown when documents are printed. We need clients to know we are user friendly and caring - and not head up our rears ends as some lawyers appear to be.
Updates

Thank you for the feedback so far. 1. Some of the designs have too much black (We prefer darker grey & not too much.) 2. Happy for designers to play around with different colours & logo design. What we're after is a modern look and business card that people say "wow" when they pick it up.

Industry/Entity Type

Business

```html
<!DOCTYPE html>
<html lang="en">
<head>
<meta charset="utf-8">
<title>Harwick Legal – Business Card</title>
<link href="https://fonts.googleapis.com/css2?family=Exo+2:wght@400;500;600&display=swap" rel="stylesheet">
<style>
  :root {
    --bg: #e6e4e1;
    --card-white: #ffffff;
    --band-dark: #111111;
    --accent-orange: #e8763a;
    --ink-dark: #2a2a2a;
    --ink-mid: #555555;
    --ink-light: #ffffff;
  }
  html, body {
    margin: 0;
    padding: 0;
    width: 1200px;
    height: 900px;
    overflow: hidden;
    background: var(--bg);
    font-family: "Exo 2", sans-serif;
  }
  .card {
    position: absolute;
    left: 100px;
    top: 150px;
    width: 1000px;
    height: 600px;
    border-radius: 56px;
    overflow: hidden;
    background: var(--card-white);
    box-shadow: 0 10px 30px rgba(0,0,0,0.18);
  }
  .card-wave { position: absolute; inset: 0; }
  .brand {
    position: absolute;
    left: 60px;
    top: 44px;
    display: flex;
    align-items: center;
    gap: 22px;
  }
  .brand-dot {
    width: 62px;
    height: 62px;
    border-radius: 50%;
    background: var(--accent-orange);
  }
  .brand-name {
    font-size: 50px;
    font-weight: 500;
    color: var(--ink-dark);
    letter-spacing: 1px;
  }
  .person {
    position: absolute;
    left: 62px;
    top: 160px;
  }
  .person-name {
    font-size: 32px;
    font-weight: 600;
    letter-spacing: 2px;
    color: var(--ink-dark);
    text-transform: uppercase;
  }
  .person-role {
    margin-top: 4px;
    font-size: 21px;
    letter-spacing: 2px;
    color: var(--ink-mid);
    text-transform: uppercase;
  }
  .address {
    position: absolute;
    left: 62px;
    top: 366px;
    color: var(--ink-light);
    font-size: 23px;
    line-height: 40px;
    letter-spacing: 1px;
  }
  .contacts {
    position: absolute;
    right: 64px;
    top: 424px;
    list-style: none;
    margin: 0;
    padding: 0;
    color: var(--ink-light);
    font-size: 18px;
    letter-spacing: 1px;
    text-align: right;
  }
  .contacts li {
    display: flex;
    justify-content: flex-end;
    align-items: center;
    gap: 12px;
    height: 28px;
  }
  .contacts svg { width: 17px; height: 17px; flex: none; }
</style>
</head>
<body>
  <section class="card">
    <svg class="card-wave" viewBox="0 0 1000 600" width="1000" height="600" aria-hidden="true">
      <path d="M0,316 C260,318 540,372 1000,398 L1000,600 L0,600 Z" fill="var(--accent-orange)"/>
      <path d="M0,328 C260,330 540,384 1000,410 L1000,600 L0,600 Z" fill="var(--band-dark)"/>
    </svg>

    <div class="brand">
      <span class="brand-dot"></span>
      <span class="brand-name">Harwick Legal</span>
    </div>

    <div class="person">
      <div class="person-name">Daniel Ferris</div>
      <div class="person-role">Financial Advisor</div>
    </div>

    <div class="address">
      <div>Suite 18, Level 3</div>
      <div>Harbour Road VIC</div>
    </div>

    <ul class="contacts">
      <li>03 9000 1234
        <svg viewBox="0 0 24 24"><path d="M6 3l4 4-2 3c1 2 3 4 5 5l3-2 4 4-3 3C10 20 4 14 3 6z" fill="#fff"/></svg>
      </li>
      <li>03 9000 1235
        <svg viewBox="0 0 24 24"><rect x="7" y="2" width="10" height="20" rx="2" fill="none" stroke="#fff" stroke-width="2"/><circle cx="12" cy="18" r="1.2" fill="#fff"/></svg>
      </li>
      <li>03 9000 1236
        <svg viewBox="0 0 24 24"><rect x="4" y="9" width="16" height="11" fill="#fff"/><rect x="7" y="3" width="10" height="7" fill="none" stroke="#fff" stroke-width="2"/></svg>
      </li>
      <li>daniel@harwick.example.au
        <svg viewBox="0 0 24 24"><rect x="3" y="6" width="18" height="12" fill="none" stroke="#fff" stroke-width="2"/><path d="M3 6l9 7 9-7" fill="none" stroke="#fff" stroke-width="2"/></svg>
      </li>
      <li>www.Harwicklegal.example.au
        <svg viewBox="0 0 24 24"><circle cx="12" cy="12" r="9" fill="none" stroke="#fff" stroke-width="2"/><path d="M3 12h18M12 3c-4 5-4 13 0 18M12 3c4 5 4 13 0 18" fill="none" stroke="#fff" stroke-width="1.5"/></svg>
      </li>
    </ul>
  </section>
</body>
</html>
```